Flyer-Design für Physiotherapie-Praxis
Zielgruppe
Wir sind eine Praxis für Physiotherapie und möchten durch diesen Flyer neue Patienten werben. Der Flyer soll in Arztpraxen ausliegen und dort den Patienten direkt ansprechen und auf uns aufmerksam machen. Es ist auch eine Verknüpfung der Therapie mit einem Training in einem Gesundheitsstudio möglich, da im gleichen Haus das Physio Kraftwerk Eichenstetten beheimatet ist.
Aufgabenstellung
Der Fokus auf unsere Prinzipien (Ganzheitliche Therapie, hohes Maß an Therapiemöglichkeiten, Variation in den therapeutischen Ansätzen durch unterschiedlich fortgebildete Therapeuten, die nach den gleichen Idealen arbeiten)

```html
<!DOCTYPE html>
<html lang="de">
<head>
<meta charset="utf-8">
<title>Flyer Zentrum für Therapie &amp; Training</title>
<link rel="stylesheet" href="https://fonts.googleapis.com/css2?family=Mulish:wght@300;400;600;800&display=swap">
<style>
  :root {
    --bg: #98bad6;
    --paper: #f7f7f7;
    --paper-white: #fafafa;
    --paper-edge: #e6e6e6;
    --navy: #3a3d6a;
    --blue: #3d95c0;
    --blue-dark: #3489b5;
    --text: #55586e;
    --photo-team: #9fbfd6;
    --photo-room: #d9d2b8;
    --photo-pool: #7cc3d8;
  }
  * { box-sizing: border-box; margin: 0; padding: 0; }
  html, body { width: 1200px; height: 900px; overflow: hidden; }
  body {
    background: var(--bg);
    font-family: "Mulish", sans-serif;
    color: var(--text);
    position: relative;
  }
  .page {
    position: absolute;
    background: var(--paper);
    box-shadow: 2px 4px 8px rgba(40,70,100,.28);
    overflow: hidden;
  }

  /* Back sheet */
  .back { left: 40px; top: 328px; width: 299px; height: 425px; background: var(--paper-white); z-index: 1; }
  .back-brand {
    position: absolute; left: 0; right: 0; top: 196px;
    display: flex; flex-direction: column; align-items: center; gap: 2px;
  }
  .back-rule { position: absolute; left: 103px; width: 94px; top: 239px; border-top: 1px solid var(--blue); }
  .back-address {
    position: absolute; left: 0; right: 0; top: 254px;
    text-align: center; font-size: 6px; line-height: 8.5px; color: var(--navy);
  }

  /* Brand block */
  .brand-sub { font-size: 6.2px; color: var(--blue); letter-spacing: .3px; text-transform: uppercase; font-weight: 400; }
  .brand { display: flex; align-items: center; gap: 5px; }
  .brand-dot { width: 8px; height: 8px; border-radius: 50%; background: var(--blue); }
  .brand-name { font-weight: 600; font-size: 10px; color: var(--navy); letter-spacing: -.2px; }
  .brand-owner { font-size: 5.8px; color: var(--blue); font-weight: 400; }

  /* Cover */
  .cover { left: 188px; top: 157px; width: 300px; height: 425px; z-index: 2; }
  .cover-head {
    height: 118px; border-bottom: 2px solid var(--blue);
    display: flex; flex-direction: column; align-items: center; justify-content: flex-end;
    gap: 2px; padding-bottom: 17px;
  }
  .cover-photo {
    margin-top: 2px; height: 182px;
    background: linear-gradient(180deg, #7f9db8 0%, var(--photo-team) 40%, #b8cfe0 100%);
  }
  .cover-band {
    position: absolute; left: 0; right: 0; bottom: 0; height: 121px;
    background: linear-gradient(180deg, #4aa0c9, var(--blue-dark));
    border-top: 3px solid #fff;
    display: flex; flex-direction: column; align-items: center; padding-top: 27px;
    color: #fff; text-align: center;
  }
  .cover-band .line1 { font-weight: 300; font-size: 16px; letter-spacing: 1px; }
  .cover-band .line2 { font-weight: 800; font-size: 16px; letter-spacing: 1px; margin-top: 2px; }

  /* Spread */
  .spread-left { left: 556px; top: 150px; width: 302px; height: 427px; background: linear-gradient(90deg, var(--paper) 88%, var(--paper-edge)); }
  .spread-right { left: 858px; top: 150px; width: 302px; height: 427px; background: linear-gradient(90deg, var(--paper-edge), var(--paper) 10%); }
  .intro-head {
    position: absolute; left: 76px; width: 98px; top: 40px;
    text-align: right; font-weight: 800; font-size: 7px; line-height: 8.6px; color: var(--navy);
    text-transform: uppercase;
  }
  .intro-rule { position: absolute; left: 81px; width: 93px; top: 91px; border-top: 1px solid var(--blue); }
  .room-photo {
    position: absolute; left: 0; width: 174px; top: 109px; height: 281px;
    background: linear-gradient(160deg, #e6dcb8, var(--photo-room) 55%, #8d8a86 100%);
  }
  .col {
    position: absolute; font-size: 5.9px; line-height: 8.6px; font-weight: 400; color: var(--text);
    hyphens: auto;
  }
  .col p + p { margin-top: 8.6px; }
  .col h3 { font-weight: 800; font-size: 7px; line-height: 8.6px; color: var(--navy); text-transform: uppercase; margin: 21px 0 9px; }
  .left-col { left: 184px; width: 93px; top: 40px; }
  .right-title {
    position: absolute; left: 29px; top: 40px;
    font-weight: 800; font-size: 10.5px; line-height: 11.5px; color: var(--navy); text-transform: uppercase;
  }
  .right-col1 { left: 29px; width: 114px; top: 83px; }
  .right-rule { position: absolute; left: 151px; top: 37px; height: 133px; border-left: 1px solid var(--blue); }
  .right-col2 { left: 163px; width: 116px; top: 39px; }
  .pool-photo {
    position: absolute; left: 0; right: 0; top: 185px; height: 205px;
    background: linear-gradient(180deg, #e9eef0 0%, #cfe0d8 35%, var(--photo-pool) 65%, #38a8cc 100%);
  }
</style>
</head>
<body>
  <section class="page back" aria-label="Rückseite">
    <div class="back-brand">
      <div class="brand-sub">Zentrum für Therapie &amp; Training</div>
      <div class="brand"><span class="brand-dot"></span><span class="brand-name">Lukas Brenner &amp; Sabine Kolb</span></div>
      <div class="brand-owner">Inhaber: Sabine Kolb</div>
    </div>
    <div class="back-rule"></div>
    <div class="back-address">Adresse<br>Strasse<br>Ort</div>
  </section>

  <section class="page cover" aria-label="Titelseite">
    <header class="cover-head">
      <div class="brand-sub">Zentrum für Therapie &amp; Training</div>
      <div class="brand"><span class="brand-dot"></span><span class="brand-name">Lukas Brenner &amp; Sabine Kolb</span></div>
      <div class="brand-owner">Inhaber: Sabine Kolb</div>
    </header>
    <div class="cover-photo" role="img" aria-label="Gruppenfoto des Praxisteams in hellblauen Poloshirts im Therapieraum"></div>
    <div class="cover-band">
      <div class="line1">WIR SIND THERAPEUTEN</div>
      <div class="line2">AUS ÜBERZEUGUNG!</div>
    </div>
  </section>

  <section class="page spread-left" aria-label="Innenseite links">
    <h2 class="intro-head">Unsere Praxis gibt es seit 1969. In dieser Zeit konnten wir viel Erfahrung sammeln.</h2>
    <div class="intro-rule"></div>
    <div class="room-photo" role="img" aria-label="Behandlungsraum mit Therapieliege und Fenster"></div>
    <div class="col left-col">
      <p>Wir sind ein Team aus älteren und jüngeren Therapeuten, aus Masseuren, med. Bademeistern und Physiotherapeuten. Diese bunte Mischung beinhaltet viel Erfahrung und viel Wissen. Beides wird in regelmäßigen internen Fortbildungen ausgetauscht. So ergänzen wir uns gegenseitig. Wir arbeiten als Team Hand in Hand und schätzen das Fachwissen jedes einzelnen Kollegen.</p>
      <p>Wir sind motiviert und mit Freude bei der Arbeit, denn wir wissen, was unsere Patienten mit Hilfe der Physiotherapie erreichen können.</p>
      <h3>Vielzahl von Therapiemöglich&shy;keiten</h3>
      <p>Wir haben eine Vielzahl von Therapiegeräten und -hilfsmitteln zur Verfügung, z.B. eine Kletterwand, Sling Trainer, eine Vibrano®-Rüttelplatte, ein Slack Rack und ein Bewegungsbad! Im 32°C warmem Wasser können sich unsere Patienten besser bewegen. Mit unserem Fachwissen und unserer Erfahrung haben wir uns auf die Behandlung orthopädischer, chirurgischer und neurologischer Patienten spezialisiert.</p>
    </div>
  </section>

  <section class="page spread-right" aria-label="Innenseite rechts">
    <h2 class="right-title">Aktives<br>Gesundheits<br>Training</h2>
    <div class="col right-col1">
      <p>Für gute Fortschritte in der Therapie und die Erhaltung dieser Fortschritte ist der Weg zur sportlichen Aktivität essentiell. Diesen Weg erleichtern wir unseren Patienten durch unser Angebot des Aktiven Gesundheitstrainings. Zusätzlich zu Ihrem Rezept erhalten unsere neuen Patienten einen zusätzlichen und kostenfrei-</p>
    </div>
    <div class="right-rule"></div>
    <div class="col right-col2">
      <p>en Beratungstermin im Physio Kraftwerk Eichenstetten. In diesem Termin zeigen wir Ihnen Möglichkeiten, selbst etwas zu Ihrer Gesundung beizutragen.<br>Je nachdem, was Ihnen gerade am effektivsten hilft, trainieren Sie 6 x am Kraft-Ausdauer-Zirkel der Firma Cirvatek oder am flexomo-Zirkel. Das Training an diesen Geräten ist einfach, sicher und effektiv. Da das Training maximal 35 Minuten Zeit beansprucht ist Zeitmangel kein Argument mehr.</p>
    </div>
    <div class="pool-photo" role="img" aria-label="Bewegungsbad mit Haltegriffen, Fensterfront und Pflanzen"></div>
  </section>
</body>
</html>
```